ulmar stationary etc..
Business Card, Stationary and Envelope Design
Please upload ai or eps of your logo.
The business cards need to be double sided
Hi sir,
I submitted my design please let the feedback and suggestions
Thank you
Veltrusa

```html
<!DOCTYPE html>
<html lang="en">
<head>
<meta charset="utf-8">
<title>ulmar stationery set</title>
<link rel="stylesheet" href="https://fonts.googleapis.com/css2?family=Montserrat:wght@600;700;800&family=Arimo:wght@400;700&display=swap">
<style>
  :root {
    --ink: #141414;
    --brand-blue: #2f86e8;
    --brand-blue-light: #5aa6f5;
    --pale-blue: #dbe9f7;
    --paper: #ffffff;
    --grey-text: #4a4a4a;
    --edge: #d4d4d4;
  }
  * { margin: 0; padding: 0; box-sizing: border-box; }
  html, body { width: 1200px; height: 857px; overflow: hidden; background: var(--paper); }
  .canvas { position: relative; width: 1200px; height: 857px; font-family: "Arimo", Arial, sans-serif; color: var(--ink); }

  .wordmark { font-family: "Montserrat", Arial, sans-serif; font-weight: 800; color: var(--ink); line-height: 1; letter-spacing: -0.02em; }
  .tagline { font-family: "Montserrat", Arial, sans-serif; font-weight: 600; color: var(--ink); letter-spacing: 0.22em; line-height: 1; }

  .master-logo { position: absolute; left: 53px; top: 30px; }
  .master-logo .wordmark { font-size: 150px; }
  .master-logo .tagline { font-size: 25px; margin-top: 8px; padding-left: 28px; }

  .sheet { position: absolute; background: var(--paper); border: 1px solid var(--edge); box-shadow: 0 2px 6px rgba(0,0,0,0.18); overflow: hidden; }

  .envelope { left: 29px; top: 228px; width: 530px; height: 276px; }
  .envelope .flap { position: absolute; left: 0; top: 0; width: 530px; height: 100px; }

  .letterhead-landscape { left: 29px; top: 540px; width: 530px; height: 276px; }
  .letterhead-portrait { left: 595px; top: 12px; width: 581px; height: 816px; }

  .sheet-logo { position: absolute; }
  .sheet-logo .wordmark { font-size: 44px; }
  .sheet-logo .tagline { font-size: 7px; margin-top: 3px; padding-left: 6px; letter-spacing: 0.3em; }

  .dash-rule { position: absolute; }

  .faint-mark { position: absolute; border-radius: 50%; background: radial-gradient(circle at 40% 40%, #eef5fc, var(--pale-blue)); opacity: 0.7; }

  .card { position: absolute; box-shadow: 0 2px 6px rgba(0,0,0,0.25); overflow: hidden; }
  .card-front { left: 619px; top: 168px; width: 341px; height: 192px; background: linear-gradient(180deg, var(--brand-blue-light), var(--brand-blue)); }
  .card-front .card-logo { position: absolute; left: 38px; top: 56px; }
  .card-front .wordmark { font-size: 74px; }
  .card-front .tagline { font-size: 14px; margin-top: 6px; padding-left: 40px; }

  .card-back { left: 708px; top: 396px; width: 377px; height: 204px; background: var(--paper); border: 1px solid var(--edge); }
  .card-back .sheet-logo { left: 14px; top: 10px; }
  .card-back .wordmark { font-size: 30px; }
  .card-back .tagline { font-size: 5px; }
  .holder-name { position: absolute; left: 20px; top: 64px; font-size: 19px; font-weight: 400; }
  .holder-role { position: absolute; left: 20px; top: 86px; font-size: 10px; color: var(--grey-text); }
  .contact-list { position: absolute; left: 20px; top: 128px; font-size: 7px; line-height: 11px; color: var(--grey-text); display: grid; grid-template-columns: 46px auto; }
</style>
</head>
<body>
<main class="canvas">

  <div class="master-logo">
    <div class="wordmark">ulmar</div>
    <div class="tagline">CLOUD COMPUTING</div>
  </div>

  <section class="sheet envelope" aria-label="Envelope">
    <svg class="flap" viewBox="0 0 530 100" preserveAspectRatio="none">
      <defs>
        <linearGradient id="flapBlue" x1="0" y1="0" x2="0" y2="1">
          <stop offset="0" stop-color="#5aa6f5"/>
          <stop offset="1" stop-color="#2f86e8"/>
        </linearGradient>
      </defs>
      <path d="M0 0 H530 V40 L280 96 Q265 100 250 96 L0 40 Z" fill="url(#flapBlue)"/>
    </svg>
  </section>

  <section class="sheet letterhead-landscape" aria-label="Letterhead">
    <div class="sheet-logo" style="left:22px; top:20px;">
      <div class="wordmark" style="font-size:40px;">ulmar</div>
      <div class="tagline">CLOUD COMPUTING</div>
    </div>
    <svg class="dash-rule" style="left:190px; top:46px;" width="330" height="10" viewBox="0 0 330 10">
      <g fill="#2f86e8">
        <rect x="0" y="2" width="40" height="6"/>
        <rect x="48" y="2" width="30" height="6" opacity="0.9"/>
        <rect x="86" y="2" width="22" height="6" opacity="0.8"/>
        <rect x="116" y="2" width="16" height="6" opacity="0.7"/>
        <rect x="140" y="2" width="12" height="6" opacity="0.6"/>
        <rect x="160" y="2" width="9" height="6" opacity="0.5"/>
        <rect x="177" y="2" width="7" height="6" opacity="0.45"/>
        <rect x="192" y="2" width="5" height="6" opacity="0.4"/>
        <rect x="205" y="2" width="4" height="6" opacity="0.35"/>
        <rect x="217" y="2" width="3" height="6" opacity="0.3"/>
        <rect x="228" y="2" width="3" height="6" opacity="0.25"/>
        <rect x="239" y="2" width="2" height="6" opacity="0.2"/>
      </g>
    </svg>
    <div class="faint-mark" style="left:340px; top:170px; width:96px; height:96px;"></div>
  </section>

  <section class="sheet letterhead-portrait" aria-label="Letterhead">
    <div class="sheet-logo" style="left:24px; top:36px;">
      <div class="wordmark">ulmar</div>
      <div class="tagline">CLOUD COMPUTING</div>
    </div>
    <svg class="dash-rule" style="left:180px; top:140px;" width="390" height="10" viewBox="0 0 390 10">
      <g fill="#2f86e8">
        <rect x="0" y="2" width="48" height="7"/>
        <rect x="58" y="2" width="36" height="7" opacity="0.9"/>
        <rect x="104" y="2" width="26" height="7" opacity="0.8"/>
        <rect x="140" y="2" width="19" height="7" opacity="0.7"/>
        <rect x="169" y="2" width="14" height="7" opacity="0.6"/>
        <rect x="193" y="2" width="10" height="7" opacity="0.5"/>
        <rect x="213" y="2" width="8" height="7" opacity="0.45"/>
        <rect x="231" y="2" width="6" height="7" opacity="0.4"/>
        <rect x="247" y="2" width="5" height="7" opacity="0.35"/>
        <rect x="262" y="2" width="4" height="7" opacity="0.3"/>
        <rect x="276" y="2" width="3" height="7" opacity="0.25"/>
        <rect x="289" y="2" width="3" height="7" opacity="0.2"/>
      </g>
    </svg>
    <div class="faint-mark" style="left:300px; top:560px; width:250px; height:250px;"></div>
  </section>

  <section class="card card-front" aria-label="Business card front">
    <div class="card-logo">
      <div class="wordmark">ulmar</div>
      <div class="tagline">CLOUD COMPUTING</div>
    </div>
  </section>

  <section class="card card-back" aria-label="Business card back">
    <div class="faint-mark" style="left:250px; top:50px; width:110px; height:110px;"></div>
    <div class="sheet-logo">
      <div class="wordmark">ulmar</div>
      <div class="tagline">CLOUD COMPUTING</div>
    </div>
    <div class="holder-name">John Doe</div>
    <div class="holder-role">Founder</div>
    <div class="contact-list">
      <span>Address</span><span>48 Corran Street, Veltmoor 07410</span>
      <span>Tel/Fax</span><span>1-555-0148-2290</span>
      <span>Phone</span><span>1-555-0176-3341</span>
      <span>Email</span><span>jdoe@ulmar.com</span>
      <span>Web address</span><span>www.ulmar.com</span>
    </div>
  </section>

</main>
</body>
</html>
```